Music Festival in Colorado Needs Awesome Flier Design

We need an eye-catching & captivating flier design for an annual music festival in Denver, CO (USA). The festival features the best Colorado musicians within the genres of jam - funk - bluegrass - electronic - reggae - rock.

The design should look clean and professional while still being creative and unique. The past three years' flier designs are attached, as well as the logo and some other designs that match the aesthetic of what we're looking for.

This festival has a big element of Colorado pride so any

Target Market(s)

Hippies - live music enthusiasts - partiers. Ages 21 - 40.

Industry/Entity Type

Entertainment

Colors
0355a3
ec1f27
ffffff
fbed22

Requirements
Must have
• Attached design text.
Nice to have
• - Quality texture and psychedelic elements.
• - Colorado pride elements; color scheme (red, white, blue & yellow), flag, ect.
• - Nature elements are awesome but this is also a downtown festival so keep that in mind.
Should not have
• Cheesy artwork.

```html
<!DOCTYPE html>
<html lang="en">
<head>
<meta charset="utf-8">
<title>Pass The Sound Music Festival</title>
<link href="https://fonts.googleapis.com/css2?family=Questrial&display=swap" rel="stylesheet">
<style>
  :root {
    --navy: #1b1a31;
    --navy-soft: #2a2b4a;
    --yellow: #fff200;
    --magenta: #d4217f;
    --purple: #7b2d8e;
    --sky: #29a6e3;
    --white: #ffffff;
  }
  html, body { margin: 0; padding: 0; overflow: hidden; background: var(--navy); }
  .flyer {
    position: relative;
    width: 848px;
    height: 1200px;
    overflow: hidden;
    background: var(--navy);
    font-family: "Questrial", sans-serif;
    color: var(--white);
  }
  .backdrop { position: absolute; inset: 0; width: 848px; height: 1200px; }
  .brand {
    position: absolute;
    left: 110px; top: 95px;
    width: 320px;
    text-align: center;
    color: var(--navy);
    font-size: 58px;
    line-height: 0.95;
    text-transform: uppercase;
    letter-spacing: 1px;
  }
  .headline {
    position: absolute;
    left: 0; top: 462px;
    width: 868px;
    text-align: center;
    line-height: 1;
  }
  .headline .line-1 { display: block; color: var(--yellow); font-size: 108px; letter-spacing: -1px; }
  .headline .line-2 { display: block; color: var(--white); font-size: 62px; margin-top: -6px; }
  .headline .line-3 { display: block; color: var(--magenta); font-size: 80px; margin-top: 4px; }
  .date-bar {
    position: absolute;
    left: 150px; top: 732px;
    width: 580px; height: 48px;
    background: var(--magenta);
    color: var(--white);
    font-size: 29px;
    line-height: 48px;
    text-align: center;
  }
  .date-bar::before, .date-bar::after {
    content: ""; position: absolute; width: 0; height: 0;
  }
  .date-bar::before { left: 0; top: 0; border-top: 16px solid var(--yellow); border-right: 16px solid transparent; }
  .date-bar::after { right: 0; bottom: 0; border-bottom: 16px solid var(--yellow); border-left: 16px solid transparent; }
  .lineup {
    position: absolute;
    left: 55px; top: 818px;
    width: 738px;
    margin: 0;
    font-size: 29.5px;
    line-height: 40px;
    text-align: justify;
  }
  .venue, .tickets { position: absolute; top: 1074px; }
  .venue { left: 116px; }
  .tickets { left: 482px; }
  .venue .name, .tickets .label { font-size: 27.5px; display: block; line-height: 32px; }
  .venue .address { font-size: 15.5px; display: block; margin-top: 2px; }
  .tickets .url { font-size: 15.5px; display: block; margin-top: 2px; color: var(--yellow); }
  .divider {
    position: absolute; left: 439px; top: 1056px;
    width: 2px; height: 88px;
    background: linear-gradient(to bottom, transparent, var(--white), transparent);
  }
</style>
</head>
<body>
<main class="flyer">
  <svg class="backdrop" viewBox="0 0 919 1300" preserveAspectRatio="none" aria-hidden="true">
    <defs>
      <radialGradient id="stage-glow" cx="0.5" cy="0.45" r="0.55">
        <stop offset="0" stop-color="#3a3c60"/>
        <stop offset="1" stop-color="#1b1a31" stop-opacity="0"/>
      </radialGradient>
      <clipPath id="badge-clip"><circle cx="850" cy="60" r="95"/></clipPath>
    </defs>
    <rect width="919" height="1300" fill="var(--navy)"/>
    <rect class="stage-photo" x="180" y="300" width="740" height="1000" fill="url(#stage-glow)" role="img" aria-label="Photo of a guitarist performing on stage"/>
    <polygon class="corner-yellow" points="0,0 510,0 735,210 0,592" fill="var(--yellow)"/>
    <polygon class="stripe-magenta" points="510,0 575,0 919,330 919,395" fill="var(--magenta)"/>
    <polygon class="stripe-purple" points="692,245 712,245 919,430 919,450" fill="var(--purple)"/>
    <polygon class="stripe-yellow" points="750,345 790,345 919,460 919,500" fill="var(--yellow)"/>
    <g class="dash-lines" stroke="var(--white)" stroke-width="2" stroke-dasharray="10 8">
      <line x1="600" y1="0" x2="760" y2="150"/>
      <line x1="650" y1="265" x2="895" y2="525"/>
    </g>
    <g class="striped-circle" clip-path="url(#badge-clip)" stroke="var(--sky)" stroke-width="16">
      <line x1="740" y1="60" x2="860" y2="-60"/>
      <line x1="740" y1="100" x2="900" y2="-60"/>
      <line x1="740" y1="140" x2="940" y2="-60"/>
      <line x1="760" y1="160" x2="960" y2="-40"/>
      <line x1="800" y1="160" x2="960" y2="0"/>
      <line x1="840" y1="160" x2="960" y2="40"/>
    </g>
    <g class="corner-stripes" fill="var(--yellow)">
      <polygon points="0,1090 0,1120 180,1300 150,1300"/>
      <polygon points="0,1150 0,1210 90,1300 30,1300"/>
    </g>
  </svg>

  <div class="brand">Pass The<br>Sound</div>

  <h1 class="headline">
    <span class="line-1">Pass</span>
    <span class="line-2">The Sound</span>
    <span class="line-3">Music Festival</span>
  </h1>

  <div class="date-bar">May 11th - 13th, 2018 (6th Annual)</div>

  <p class="lineup">Jess Ashford Band, Anyone Ensemble, Split Theory, The Lucky Sprouts, J-Ray &amp; The Summit, Tallgrass, Kinetics, Elevation Ensemble Sunsoaked, Parasonics, Spectral, Clear Signal, Rail Junction, Orbits.</p>

  <div class="venue">
    <span class="name">Elm Street Yard</span>
    <span class="address">410 W. 52nd Ave Denver, CO 80221</span>
  </div>
  <div class="divider"></div>
  <div class="tickets">
    <span class="label">Tickets &amp; More Info</span>
    <span class="url">www.passthesoundfest.com</span>
  </div>
</main>
</body>
</html>
```